Dalwick Self Storage Billboard

This is a 12'x24' billboard. I need this billboard to scream that it is for self storage with part of or all of the billboard having a picture of a storage unit or storage units in the background that matches my logo colors. You can use a stock image for this or I attached a picture if you would want to use that. I also need the billboard to include my logo which I have attached, the phone number of 555-014-2736, and I would like the billboard to say the following:
-Rent 100% Online at DalwickSelfStorage.example (emphasize this)
-Drive-Up & Temp-Controlled Units
-Covered & Uncovered Boat/RV Parking

I would also like there to be an arrow pointing LEFT on the bottom of the billboard that says: Millbrook Landing Apartments | 555-014-2736

```html
<!DOCTYPE html>
<html lang="en">
<head>
<meta charset="utf-8">
<title>Dalwick Self Storage Billboard</title>
<link rel="stylesheet" href="https://fonts.googleapis.com/css2?family=Barlow+Condensed:wght@400;600;700&family=Montserrat:wght@500&display=swap">
<style>
  :root {
    --page: #ececec;
    --navy: #0b1d3a;
    --navy-light: #173c6e;
    --blue: #1558a8;
    --brand-blue: #1a5cab;
    --white: #ffffff;
    --ink: #0e1f3b;
  }
  html, body {
    margin: 0;
    width: 1154px;
    height: 1200px;
    overflow: hidden;
    background: var(--page);
  }
  .billboard {
    position: absolute;
    left: 20px;
    top: 323px;
    width: 1458px;
    height: 725px;
    transform: scale(0.7641);
    transform-origin: 0 0;
    overflow: hidden;
    box-shadow: 0 10px 30px rgba(0,0,0,0.18);
  }
  .billboard-shapes {
    position: absolute;
    inset: 0;
    width: 1458px;
    height: 725px;
  }
  .brand {
    position: absolute;
    left: 80px;
    top: 62px;
    display: flex;
    align-items: center;
    gap: 22px;
  }
  .brand-mark {
    width: 84px;
    height: 84px;
    background: var(--brand-blue);
  }
  .brand-name {
    font-family: "Barlow Condensed", sans-serif;
    font-weight: 700;
    font-size: 54px;
    color: var(--brand-blue);
    line-height: 1;
    white-space: nowrap;
  }
  .headline {
    position: absolute;
    left: 72px;
    top: 222px;
    margin: 0;
    font-family: "Barlow Condensed", sans-serif;
    font-weight: 700;
    font-size: 128px;
    line-height: 1;
    letter-spacing: 1px;
    background: linear-gradient(180deg, #ffffff 0%, #ffffff 48%, #cfd3d8 58%, #ffffff 100%);
    -webkit-background-clip: text;
    background-clip: text;
    color: transparent;
    white-space: nowrap;
  }
  .online-at {
    position: absolute;
    left: 90px;
    top: 343px;
    width: 465px;
    display: flex;
    align-items: center;
    gap: 22px;
    font-family: "Barlow Condensed", sans-serif;
    font-weight: 400;
    font-size: 48px;
    color: var(--white);
    line-height: 1;
  }
  .online-at::before, .online-at::after {
    content: "";
    flex: 1;
    height: 3px;
    background: linear-gradient(90deg, transparent, var(--blue), transparent);
  }
  .web-pill {
    position: absolute;
    left: 62px;
    top: 405px;
    width: 530px;
    height: 63px;
    box-sizing: border-box;
    border: 3px solid var(--white);
    border-radius: 32px;
    background: linear-gradient(90deg, #a9adb2 0%, #f6f6f6 40%, #e6e7e9 70%, #a9adb2 100%);
    display: flex;
    align-items: center;
    justify-content: center;
    gap: 12px;
    box-shadow: 0 4px 10px rgba(0,0,0,0.35);
  }
  .web-pill svg { width: 36px; height: 36px; }
  .web-address {
    font-family: "Barlow Condensed", sans-serif;
    font-weight: 600;
    font-size: 40px;
    color: var(--ink);
    line-height: 1;
  }
  .features {
    position: absolute;
    left: 88px;
    top: 494px;
    margin: 0;
    padding: 0;
    list-style: none;
  }
  .features li {
    display: flex;
    align-items: center;
    gap: 18px;
    height: 51px;
    font-family: "Montserrat", sans-serif;
    font-weight: 500;
    font-size: 28px;
    color: var(--white);
  }
  .features svg { width: 30px; height: 30px; }
  .direction {
    position: absolute;
    left: 148px;
    top: 619px;
    font-family: "Barlow Condensed", sans-serif;
    font-weight: 600;
    font-size: 54px;
    line-height: 58px;
    color: var(--white);
    white-space: nowrap;
  }
  .phone {
    position: absolute;
    left: 900px;
    top: 610px;
    display: flex;
    align-items: center;
    gap: 20px;
  }
  .phone svg { width: 66px; height: 66px; }
  .phone-number {
    font-family: "Barlow Condensed", sans-serif;
    font-weight: 700;
    font-size: 84px;
    line-height: 1;
    color: var(--ink);
    white-space: nowrap;
  }
</style>
</head>
<body>
  <div class="billboard">
    <svg class="billboard-shapes" viewBox="0 0 1458 725" xmlns="http://www.w3.org/2000/svg">
      <defs>
        <linearGradient id="band-navy" x1="0" y1="0" x2="1" y2="0">
          <stop offset="0" stop-color="#0b1d3a"/>
          <stop offset="1" stop-color="#173c6e"/>
        </linearGradient>
        <linearGradient id="top-white" x1="0" y1="0" x2="1" y2="0">
          <stop offset="0.45" stop-color="#ffffff"/>
          <stop offset="1" stop-color="#e4e5e7"/>
        </linearGradient>
        <linearGradient id="photo-tones" x1="0" y1="0" x2="0" y2="1">
          <stop offset="0" stop-color="#7fb0e3"/>
          <stop offset="0.22" stop-color="#c7dcf1"/>
          <stop offset="0.3" stop-color="#2a6fc4"/>
          <stop offset="0.6" stop-color="#1f63b8"/>
          <stop offset="0.68" stop-color="#4d4f54"/>
          <stop offset="1" stop-color="#3d3f44"/>
        </linearGradient>
        <linearGradient id="silver" x1="0" y1="0" x2="1" y2="0">
          <stop offset="0" stop-color="#b9bcc0"/>
          <stop offset="0.45" stop-color="#f6f6f6"/>
          <stop offset="1" stop-color="#c9ccd0"/>
        </linearGradient>
        <clipPath id="photo-clip">
          <path d="M870,0 L1458,0 L1458,725 L885,725 C780,620 725,470 725,330 C725,190 790,70 870,0 Z"/>
        </clipPath>
      </defs>

      <rect class="top-panel" x="0" y="0" width="1458" height="212" fill="url(#top-white)"/>
      <rect class="headline-band" x="0" y="212" width="1458" height="226" fill="url(#band-navy)"/>
      <rect class="feature-band" x="0" y="438" width="1458" height="287" fill="#1558a8"/>

      <path class="arrow" d="M65,648 L120,598 L120,615 L860,615 L860,681 L120,681 L120,698 Z" fill="#0b1d3a"/>

      <path class="swoosh-navy" d="M700,0 L1458,0 L1458,725 L790,725 C690,610 645,440 655,300 C665,170 690,60 700,0 Z" fill="#0b1d3a"/>
      <path class="swoosh-blue" d="M830,0 L1458,0 L1458,725 L860,725 C755,620 700,460 703,320 C706,180 770,60 830,0 Z" fill="#1558a8"/>

      <g clip-path="url(#photo-clip)">
        <rect class="photo" x="700" y="0" width="758" height="592" fill="url(#photo-tones)" role="img" aria-label="Photo of a row of blue roll-up storage unit doors under a blue sky"/>
        <rect class="phone-bar" x="700" y="592" width="758" height="133" fill="url(#silver)"/>
      </g>
      <path class="swoosh-line" d="M885,725 C780,620 725,470 725,330 C725,190 790,70 870,0" fill="none" stroke="#ffffff" stroke-width="7"/>
    </svg>

    <div class="brand">
      <div class="brand-mark"></div>
      <div class="brand-name">Dalwick Self Storage</div>
    </div>

    <h1 class="headline">Rent 100%</h1>
    <div class="online-at">Online at</div>

    <div class="web-pill">
      <svg viewBox="0 0 24 24" fill="none" stroke="#0e1f3b" stroke-width="1.6">
        <circle cx="12" cy="12" r="10"/>
        <ellipse cx="12" cy="12" rx="4.5" ry="10"/>
        <line x1="2" y1="12" x2="22" y2="12"/>
        <path d="M4 7h16M4 17h16"/>
      </svg>
      <span class="web-address">DalwickSelfStorage.example</span>
    </div>

    <ul class="features">
      <li>
        <svg viewBox="0 0 30 30"><circle cx="15" cy="15" r="14" fill="#0b1d3a"/><path d="M9 15.5l4 4 8-8" fill="none" stroke="#4f8fdc" stroke-width="2.6" stroke-linecap="round" stroke-linejoin="round"/></svg>
        Drive-Up &amp; Temp-Controlled Units
      </li>
      <li>
        <svg viewBox="0 0 30 30"><circle cx="15" cy="15" r="14" fill="#0b1d3a"/><path d="M9 15.5l4 4 8-8" fill="none" stroke="#4f8fdc" stroke-width="2.6" stroke-linecap="round" stroke-linejoin="round"/></svg>
        Covered &amp; Uncovered Boat/RV Parking
      </li>
    </ul>

    <div class="direction">Millbrook Landing Apartments</div>

    <div class="phone">
      <svg viewBox="0 0 66 66">
        <circle cx="33" cy="33" r="33" fill="#1558a8"/>
        <path d="M22 16c2-1 4 0 5 2l3 6c1 2 0 3-1 4l-2 2c2 5 5 8 10 10l2-2c1-1 3-2 4-1l6 3c2 1 3 3 2 5l-2 4c-1 2-4 3-7 2-11-3-21-13-24-24-1-3 0-6 2-7z" fill="#ffffff"/>
        <path d="M38 18a12 12 0 0 1 10 10M38 11a19 19 0 0 1 17 17" fill="none" stroke="#ffffff" stroke-width="2.6" stroke-linecap="round"/>
      </svg>
      <span class="phone-number">555-014-2736</span>
    </div>
  </div>
</body>
</html>
```